Ironvale Leasing Corp - Business Card Design

Need a new modern designed business card that is different and stands out to represent my equipment financing company. Ironvale Leasing Corp finances all types of equipment and all types of industries. We like to do equipment financing a different way by putting customers first and want our card to represent that different approach to business. I want a card that some remembers when they receive it so it sticks in their mind and makes that wow impression.

Card should have a black background so the logo stands out. It can be horizontial or vertical or a combination of both.

Front of card information is below that shows the information that would go on my card. That is where I want a different look or design to stand out. The front could be split black/orange colour so the logo could pop on black side and information on orange side with different lettering. Just outside the box thinking on the front of the card. Open to any type of design.

Back of card is below which i I like unless you have a different spin to provide or a different idea that would make the card better as I am open to anything that looks great.

Target Market(s)

Ironvale Leasing Corp deals with business owners in all industries.

Industry/Entity Type

Business

Contact Information for Business Card

Colors

Designer to choose colors to be used in the design.

Requirements
Must have
• Modern
• Different
• Stand Out
• Makes an Impression

```html
<!DOCTYPE html>
<html lang="en">
<head>
<meta charset="utf-8">
<title>Ironvale Leasing Corp – Business Card</title>
<link rel="stylesheet" href="https://fonts.googleapis.com/css2?family=Anton&family=Montserrat:wght@300;400;600&display=swap">
<style>
  :root {
    --page: #2a2a2c;
    --card: #0d0d0e;
    --card-edge: #1a1a1b;
    --orange: #f47a20;
    --orange-deep: #ee5a1c;
    --white: #ffffff;
    --grey: #d9d9d9;
  }
  * { box-sizing: border-box; margin: 0; padding: 0; }
  html, body { width: 1200px; height: 900px; overflow: hidden; }
  body {
    background: var(--page);
    font-family: "Montserrat", sans-serif;
    display: flex;
    flex-direction: column;
    align-items: center;
    justify-content: center;
    gap: 60px;
  }
  .card {
    position: relative;
    width: 525px;
    height: 300px;
    border-radius: 18px;
    background: linear-gradient(135deg, var(--card-edge), var(--card) 60%);
    overflow: hidden;
    box-shadow: 0 14px 30px rgba(0,0,0,.45);
  }

  /* back */
  .card-back {
    display: flex;
    flex-direction: column;
    align-items: center;
    justify-content: center;
    gap: 14px;
  }
  .brand {
    display: flex;
    align-items: center;
    gap: 10px;
    color: var(--orange);
    font-weight: 600;
    font-size: 26px;
    letter-spacing: .5px;
  }
  .brand-dot {
    width: 16px; height: 16px;
    border-radius: 50%;
    background: var(--orange);
  }
  .tagline {
    color: var(--grey);
    font-size: 12px;
    font-weight: 600;
    letter-spacing: 1.5px;
    text-transform: uppercase;
  }

  /* front */
  .front-brand {
    position: absolute;
    top: 40px;
    right: 32px;
    text-align: right;
  }
  .front-brand .brand { font-size: 17px; justify-content: flex-end; gap: 7px; }
  .front-brand .brand-dot { width: 11px; height: 11px; }
  .front-brand .tagline { font-size: 8px; letter-spacing: 1px; margin-top: 6px; }
  .rule-top {
    position: absolute;
    left: 0; top: 104px;
    width: 300px; height: 2px;
    background: var(--orange);
  }
  .person {
    position: absolute;
    left: 34px; top: 118px;
  }
  .person-name {
    font-family: "Anton", sans-serif;
    color: var(--white);
    font-size: 40px;
    line-height: 1;
    letter-spacing: .5px;
    text-transform: uppercase;
  }
  .person-role {
    color: var(--orange);
    font-size: 14px;
    font-weight: 300;
    margin-top: 2px;
  }
  .rule-mid {
    position: absolute;
    left: 0; top: 186px;
    width: 360px; height: 2px;
    background: var(--orange);
  }
  .contacts {
    position: absolute;
    left: 40px; top: 200px;
    list-style: none;
    display: flex;
    flex-direction: column;
    gap: 9px;
  }
  .contacts li {
    display: flex;
    align-items: center;
    gap: 10px;
    color: var(--white);
    font-size: 12px;
  }
  .contacts li:first-child { font-size: 14px; }
  .contacts svg { width: 16px; height: 16px; flex: none; }
  .band {
    position: absolute;
    left: 0; right: 0; bottom: 0;
    height: 16px;
    background: linear-gradient(90deg, var(--orange-deep), var(--orange));
  }
</style>
</head>
<body>

  <section class="card card-back" aria-label="Card back">
    <div class="brand"><span class="brand-dot"></span>Ironvale Leasing Corp</div>
    <p class="tagline">Equipment Financing Experts</p>
  </section>

  <section class="card card-front" aria-label="Card front">
    <div class="front-brand">
      <div class="brand"><span class="brand-dot"></span>Ironvale Leasing Corp</div>
      <p class="tagline">Equipment Financing Experts</p>
    </div>
    <div class="rule-top"></div>

    <div class="person">
      <h1 class="person-name">Owen Barlow</h1>
      <p class="person-role">President</p>
    </div>
    <div class="rule-mid"></div>

    <ul class="contacts">
      <li>
        <svg viewBox="0 0 16 16" aria-hidden="true"><path fill="#f47a20" d="M1 5c0-2 3-3 7-3s7 1 7 3v1h-3V5H4v1H1zM3 8h10l1 6H2zm5 1.5a2 2 0 1 0 0 4 2 2 0 0 0 0-4z"/></svg>
        403.555.0182
      </li>
      <li>
        <svg viewBox="0 0 16 16" aria-hidden="true"><rect x="1" y="3" width="14" height="10" fill="#f47a20"/><path d="M1 3l7 6 7-6" fill="none" stroke="#0d0d0e" stroke-width="1.3"/></svg>
        owen@ironvaleleasing.ca
      </li>
      <li>
        <svg viewBox="0 0 16 16" aria-hidden="true" fill="none" stroke="#f47a20" stroke-width="1.2"><circle cx="8" cy="8" r="6.5"/><ellipse cx="8" cy="8" rx="3" ry="6.5"/><path d="M1.5 8h13M2.5 5h11M2.5 11h11"/></svg>
        www.ironvaleleasing.ca
      </li>
    </ul>

    <div class="band"></div>
  </section>

</body>
</html>
```